Packaging label for Multi purpose ointment/balm

I would like to change packaging label (design) for multi purpose ointment (balm) that I have. Name of company is Vela Orin and I named the product (ointment) TUSKLEN. I attached pictures of existing label that i have (first file). The other 3 files are just changes that I was thinking to add. I would like to completely change look (design) of label. I was thinking to remove name TUSKLEN and make it more stand out "multi purpose ointment" instead. But word TUSKLEN can also stay on it if you think that would come out better. I was also thinking to change it to balm instead of ointment.
So I would like on label to stand out:
-multi purpose ointment or balm
-skin
-muscles
-joints
Ointment would be mostly use for skin problems, so I was thinking to add something like: cuts, burns, scrapes,... next to the word "skin".
Please feel free to use creation and completely change the look of label (design), because I want completely different design, and not similar design.
Here is description of multi purpose ointment:
Tusklen is multi purpose ointment with pain relief, anti-inflammatory and other healing properties for skin, muscles and joints. It is all natural, non-gmo, and made from the finest plant-based ingredients.
PURPOSE AND USE
Tusklen is a multi purpose ointment suitable for everyday use. It can be used to treat various injuries and phenomena of the skin such as wounds, sores, ulcers, mastitis, insect bites, burns, whitlow, herpes, aphthae, bruises, blisters and fungal infections with healing effects generally visible within 3 days. Do not apply directly on open wounds. It may be covered with a loosely wrapped sterile bandage that does not inhibit blood circulation. Tusklen also reduces swelling and relieves pain caused by rheumatism, gout, sciatica, arthritis. It can also be applied as a massage balm to improve blood circulation, reduce inflammation of muscles and ligaments, and alleviate back pain, joint pain, shoulder pain and other muscle soreness. For best results, massage affected area several times a day. In addition, the ointment can be used to effectively relieve nasal and upper respiratory congestion (apply around the nose, chest and throat). Tusklen may also be applied as a daily moisturizer to revitalize skin and prevent the formation of stretch marks. After use, the skin is soft and toned.
marlow Market(s)
Stores like brightcart, shopvane, marlow, bulkery, stores with natural products,...
Industry/Entity Type
It Company
Font styles to use
Requirements
Nice to have
- I want completely different design. Not similar design.

```html
<!DOCTYPE html>
<html lang="en">
<head>
<meta charset="UTF-8">
<title>Multi Purpose Balm – Tusklen Label</title>
<link href="https://fonts.googleapis.com/css2?family=Oswald:wght@400;500&display=swap" rel="stylesheet">
<style>
  :root {
    --page-bg: #eef0ee;
    --teal: #1fa796;
    --teal-deep: #13907f;
    --white: #ffffff;
  }
  html, body {
    margin: 0;
    width: 1200px;
    height: 1000px;
    overflow: hidden;
    background: var(--page-bg);
  }
  .canvas {
    position: relative;
    width: 1200px;
    height: 1000px;
  }
  .label {
    position: absolute;
    left: 80px;
    top: 185px;
    width: 1040px;
    height: 630px;
    box-shadow: 0 10px 30px rgba(0, 0, 0, 0.12);
  }
  .label text {
    font-family: "Oswald", sans-serif;
    text-anchor: middle;
  }
  .headline { fill: var(--teal); font-size: 100px; font-weight: 400; }
  .use-list { fill: var(--white); font-size: 60px; font-weight: 400; letter-spacing: 1px; }
  .skin-list { fill: var(--white); font-size: 46px; font-weight: 400; letter-spacing: 2px; }
  .brand-name { fill: var(--white); font-size: 34px; font-weight: 500; letter-spacing: 5px; }
</style>
</head>
<body>
<main class="canvas">
  <svg class="label" viewBox="0 0 1040 630" xmlns="http://www.w3.org/2000/svg">
    <defs>
      <linearGradient id="labelFill" x1="0" y1="0" x2="1" y2="1">
        <stop offset="0" stop-color="#1fa796"/>
        <stop offset="1" stop-color="#13907f"/>
      </linearGradient>
    </defs>

    <rect class="label-band" width="1040" height="630" fill="url(#labelFill)"/>

    <g class="title-badge">
      <circle cx="368" cy="287" r="205" fill="var(--white)"/>
      <text class="headline" x="368" y="237">MULTI</text>
      <text class="headline" x="368" y="345">PURPOSE</text>
      <text class="headline" x="368" y="453">BALM</text>
    </g>

    <g class="use-badge">
      <circle cx="720" cy="196" r="145" fill="none" stroke="var(--white)" stroke-width="6"/>
      <text class="use-list" x="720" y="134">SKIN</text>
      <text class="use-list" x="720" y="223">MUSCLES</text>
      <text class="use-list" x="720" y="310">JOINTS</text>
    </g>

    <g class="skin-badge">
      <circle cx="660" cy="480" r="125" fill="none" stroke="var(--white)" stroke-width="6"/>
      <text class="skin-list" x="660" y="450">CUTS</text>
      <text class="skin-list" x="660" y="505">BURNS</text>
      <text class="skin-list" x="660" y="560">SCRAPES</text>
    </g>

    <text class="brand-name" x="368" y="594">TUSKLEN</text>
  </svg>
</main>
</body>
</html>
```